Business Card of PebbleFinch
PebbleFinch
Bright & Fun-filled
Daniel Osei, CFA
President
412 Whitmore Suite 208
Irvine, CA 92655
daniel@pebblefinch.example
pebblefinch.example

```html
<!DOCTYPE html>
<html lang="en">
<head>
<meta charset="utf-8">
<title>PebbleFinch Stationery</title>
<link rel="stylesheet" href="https://fonts.googleapis.com/css2?family=Montserrat:wght@400;600;800&display=swap">
<style>
:root{
  --bg:#4c5676;
  --paper:#ffffff;
  --red:#e2292b;
  --yellow:#f6aa1c;
  --grey:#8c8f96;
  --ink:#3a3a3a;
  --muted:#8a8a8a;
}
*{box-sizing:border-box;margin:0;padding:0}
html,body{width:1200px;height:967px;overflow:hidden}
body{background:var(--bg);font-family:"Montserrat",sans-serif;color:var(--ink);position:relative}
.sheet{position:absolute;background:var(--paper);box-shadow:0 4px 14px rgba(0,0,0,.25);overflow:hidden}
.band-right{position:absolute;top:0;right:0;bottom:0;width:10px;background:var(--yellow)}
.band-left{position:absolute;top:0;left:0;bottom:0;width:10px;background:var(--red)}
.brand{display:flex;align-items:center;gap:5px;font-weight:800;color:var(--red);white-space:nowrap}
.brand .dot{border-radius:50%;background:var(--yellow);flex:none}
.brand-sm{font-size:11px}.brand-sm .dot{width:10px;height:10px}
.brand-md{font-size:16px}.brand-md .dot{width:14px;height:14px}
.brand-lg{font-size:22px}.brand-lg .dot{width:20px;height:20px}
.tagline{font-size:8px;color:var(--muted);margin-top:3px}
.contact{font-size:8px;line-height:1.5;color:var(--ink)}
.contact .name{font-weight:600;font-size:9px}
.center{display:flex;flex-direction:column;align-items:center;justify-content:center;height:100%}

/* business cards */
.card{width:260px;height:150px}
.card-back{left:40px;top:40px}
.card-back .brand{position:absolute;left:22px;top:22px}
.card-back .contact{position:absolute;left:22px;bottom:20px}
.card-front{left:40px;top:210px}
.card-alt{left:40px;top:380px}
.card-alt .band-right{background:var(--red)}

/* letterhead */
.letterhead{left:330px;top:40px;width:290px;height:410px}
.letterhead .brand{position:absolute;right:26px;top:26px}
.letterhead .contact{position:absolute;left:24px;top:28px;font-size:7px}

/* small pieces */
.card-small{left:650px;top:40px;width:240px;height:140px}
.card-small .brand{position:absolute;left:20px;top:20px}
.card-small .contact{position:absolute;left:20px;bottom:16px}
.slip{left:650px;top:200px;width:240px;height:110px}
.slip .brand{position:absolute;right:22px;top:18px}
.slip .contact{position:absolute;left:20px;bottom:14px}
.dl{left:650px;top:330px;width:240px;height:120px}
.dl .band-right{background:var(--red)}

/* envelopes */
.envelope{left:920px;width:240px;height:100px}
.env-yellow{top:40px;background:var(--yellow)}
.env-red{top:155px;background:var(--red)}
.env-grey{top:270px;background:var(--grey)}
.envelope svg{position:absolute;inset:0}
.env-white{left:920px;top:385px;width:240px;height:110px}
.env-white .brand{position:absolute;left:16px;top:14px}
.env-white .contact{position:absolute;left:16px;top:36px;font-size:7px}

/* folder */
.folder{left:40px;top:540px;width:560px;height:390px}
.folder .brand{position:absolute;right:30px;top:28px}
.folder .contact{position:absolute;left:330px;top:28px;font-size:7px}
.folder svg{position:absolute;left:0;bottom:0}
.folder .center-brand{position:absolute;left:230px;top:210px}

/* disc + sleeve */
.sleeve{left:650px;top:690px;width:230px;height:240px}
.sleeve .center{padding-top:60px}
.disc{position:absolute;left:665px;top:530px;width:200px;height:200px}

/* fax */
.fax{left:920px;top:520px;width:240px;height:410px}
.fax .brand{position:absolute;right:26px;top:22px}
.fax h2{position:absolute;left:22px;top:62px;font-size:26px;font-weight:800;color:var(--ink)}
.fax-fields{position:absolute;left:22px;right:26px;top:110px;font-size:8px;border-collapse:collapse}
.fax-fields td{padding:5px 0;border-bottom:1px solid #cfcfcf}
.fax-fields td:first-child{width:44px;font-weight:600}
</style>
</head>
<body>

<div class="sheet card card-back">
  <div class="brand brand-md"><span class="dot"></span>PebbleFinch</div>
  <div class="contact">
    <div class="name">Daniel Osei, CFA</div>
    <div>President</div>
    <div>412 Whitmore Suite 208, Irvine, CA 92655</div>
    <div>daniel@pebblefinch.example</div>
  </div>
  <div class="band-right"></div>
</div>

<div class="sheet card card-front">
  <div class="center">
    <div class="brand brand-lg"><span class="dot"></span>PebbleFinch</div>
    <div class="tagline">Bright &amp; Fun-filled</div>
  </div>
  <div class="band-right"></div>
</div>

<div class="sheet card card-alt">
  <div class="center">
    <div class="brand brand-lg"><span class="dot"></span>PebbleFinch</div>
    <div class="tagline">pebblefinch.example</div>
  </div>
  <div class="band-right"></div>
</div>

<div class="sheet letterhead">
  <div class="contact">
    <div>412 Whitmore Suite 208</div>
    <div>Irvine, CA 92655</div>
  </div>
  <div class="brand brand-sm"><span class="dot"></span>PebbleFinch</div>
  <div class="band-right"></div>
</div>

<div class="sheet card-small">
  <div class="brand brand-sm"><span class="dot"></span>PebbleFinch</div>
  <div class="contact">
    <div class="name">Daniel Osei, CFA</div>
    <div>daniel@pebblefinch.example</div>
  </div>
  <div class="band-right"></div>
</div>

<div class="sheet slip">
  <div class="brand brand-sm"><span class="dot"></span>PebbleFinch</div>
  <div class="contact"><div>pebblefinch.example</div></div>
  <div class="band-right"></div>
</div>

<div class="sheet dl">
  <div class="center">
    <div class="brand brand-md"><span class="dot"></span>PebbleFinch</div>
  </div>
  <div class="band-right"></div>
</div>

<div class="sheet envelope env-yellow">
  <svg width="240" height="100"><polygon points="0,0 240,0 120,55" fill="#ffffff" opacity=".25"/></svg>
</div>
<div class="sheet envelope env-red">
  <svg width="240" height="100"><polygon points="0,0 240,0 120,55" fill="#ffffff" opacity=".25"/></svg>
</div>
<div class="sheet envelope env-grey">
  <svg width="240" height="100"><polygon points="0,0 240,0 120,55" fill="#ffffff" opacity=".25"/></svg>
</div>
<div class="sheet env-white">
  <div class="brand brand-sm"><span class="dot"></span>PebbleFinch</div>
  <div class="contact"><div>412 Whitmore Suite 208</div><div>Irvine, CA 92655</div></div>
</div>

<div class="sheet folder">
  <div class="band-left"></div>
  <div class="contact"><div>412 Whitmore Suite 208</div><div>Irvine, CA 92655</div></div>
  <div class="brand brand-sm"><span class="dot"></span>PebbleFinch</div>
  <div class="center-brand brand brand-sm"><span class="dot"></span>PebbleFinch</div>
  <svg width="560" height="130" viewBox="0 0 560 130">
    <polygon points="0,130 0,20 60,0 150,0 150,130" fill="var(--yellow)"/>
    <polygon points="150,130 150,40 560,40 560,130" fill="#f4f4f4"/>
    <rect x="0" y="0" width="10" height="130" fill="var(--red)"/>
  </svg>
</div>

<div class="sheet sleeve">
  <div class="center">
    <div class="brand brand-sm"><span class="dot"></span>PebbleFinch</div>
  </div>
  <div class="band-right"></div>
</div>

<svg class="disc" viewBox="0 0 200 200">
  <circle cx="100" cy="100" r="98" fill="var(--yellow)"/>
  <path d="M100 2 A98 98 0 0 0 100 198 Z" fill="var(--red)"/>
  <circle cx="100" cy="100" r="26" fill="#ffffff"/>
  <circle cx="100" cy="100" r="9" fill="var(--bg)"/>
</svg>

<div class="sheet fax">
  <div class="brand brand-sm"><span class="dot"></span>PebbleFinch</div>
  <h2>Fax</h2>
  <table class="fax-fields">
    <tr><td>To</td><td></td></tr>
    <tr><td>From</td><td></td></tr>
    <tr><td>Fax</td><td></td></tr>
    <tr><td>Phone</td><td></td></tr>
    <tr><td>Date</td><td></td></tr>
    <tr><td>Pages</td><td></td></tr>
    <tr><td>Re</td><td></td></tr>
  </table>
  <div class="band-right"></div>
</div>

</body>
</html>
```